We need a logo for our business which is a dental clinic (i.e. dentistry).
We would lilke designs using the colour blue, green and black incorporating the words Corvasta Dental, possibly a smile or a tooth image can be considered for incorporation in the logo.

Industry/Entity Type

Dental

```html
<!DOCTYPE html>
<html lang="en">
<head>
<meta charset="utf-8">
<title>Corvasta Dental – Business Cards</title>
<link href="https://fonts.googleapis.com/css2?family=PT+Sans+Narrow:wght@400;700&family=Arimo:ital,wght@0,400;1,400&display=swap" rel="stylesheet">
<style>
  :root {
    --backdrop: #e6e7e9;
    --card-dark: #3a3a3c;
    --rule: #6a6a6d;
    --text-light: #e9e9ea;
    --blue: #0aaacd;
    --green: #0daa4f;
    --white: #ffffff;
  }
  * { margin: 0; padding: 0; box-sizing: border-box; }
  html, body { width: 1200px; height: 900px; overflow: hidden; }
  body { background: var(--backdrop); position: relative; font-family: "Arimo", Arial, sans-serif; }

  .business-card {
    position: absolute; left: 308px; width: 601px; height: 332px;
    background: var(--card-dark); overflow: hidden;
  }
  .business-card--blue { top: 58px; --accent: var(--blue); }
  .business-card--green { top: 479px; --accent: var(--green); }

  .card-shapes { position: absolute; inset: 0; }

  .holder-name {
    position: absolute; left: 23px; top: 86px;
    font-family: "PT Sans Narrow", "Arial Narrow", sans-serif;
    font-size: 35px; color: var(--accent); letter-spacing: -0.5px; line-height: 1;
  }
  .holder-role {
    position: absolute; right: 375px; top: 123px;
    font-family: "PT Sans Narrow", "Arial Narrow", sans-serif;
    font-size: 20px; color: var(--text-light); line-height: 1;
  }

  .contact-list { position: absolute; left: 17px; top: 235px; font-size: 13.5px; color: var(--text-light); line-height: 22px; }
  .contact-phones { display: flex; gap: 18px; align-items: center; }
  .contact-item { display: flex; align-items: center; gap: 4px; }
  .contact-item svg { display: block; }

  .opening-hours {
    position: absolute; left: 272px; top: 257px; display: flex; align-items: center; gap: 4px;
    font-size: 14px; color: var(--text-light);
  }

  .web-address {
    position: absolute; left: 11px; top: 311px;
    font-size: 13px; font-style: italic; letter-spacing: 16.2px; color: var(--accent);
    white-space: nowrap;
  }

  .brand-name {
    position: absolute; left: 524px; top: 12px; height: 232px; width: 56px;
    writing-mode: vertical-rl; transform: rotate(180deg);
    font-family: "PT Sans Narrow", "Arial Narrow", sans-serif; font-weight: 700;
    font-size: 38px; line-height: 56px; color: var(--white); text-align: center; white-space: nowrap;
  }
</style>
</head>
<body>

<section class="business-card business-card--blue" aria-label="Business card, blue version">
  <svg class="card-shapes" width="601" height="332" viewBox="0 0 601 332" aria-hidden="true">
    <path d="M469 0 H601 V332 L492 266 Q469 252 469 228 Z" fill="var(--accent)"/>
    <rect x="0" y="89" width="15" height="29" fill="var(--accent)"/>
    <line x1="0" y1="229.5" x2="452" y2="229.5" stroke="var(--rule)" stroke-width="1"/>
    <line x1="260.5" y1="238" x2="260.5" y2="295" stroke="var(--rule)" stroke-width="1"/>
    <polyline points="0,304.5 512,304.5 548,332" fill="none" stroke="var(--rule)" stroke-width="1"/>
    <circle cx="552" cy="268" r="13" fill="none" stroke="var(--white)" stroke-width="4"/>
  </svg>
  <p class="holder-name">Dr Nolan Hale</p>
  <p class="holder-role">Director</p>
  <div class="contact-list">
    <div class="contact-phones">
      <span class="contact-item">
        <svg width="18" height="18" viewBox="0 0 18 18" aria-hidden="true"><circle cx="9" cy="9" r="8" fill="none" stroke="var(--text-light)" stroke-width="1.4"/><path d="M6 4.5 L7.6 6.8 L6.8 7.8 Q7.8 10.2 10.2 11.2 L11.2 10.4 L13.5 12 L12.4 13.4 Q8.5 13.4 5.6 9.6 Q4.4 7 6 4.5 Z" fill="var(--text-light)"/></svg>
        555-210-4837
      </span>
      <span class="contact-item">
        <svg width="12" height="20" viewBox="0 0 12 20" aria-hidden="true"><rect x="1" y="1" width="10" height="18" rx="1.5" fill="none" stroke="var(--text-light)" stroke-width="1.4"/><line x1="4" y1="16" x2="8" y2="16" stroke="var(--text-light)" stroke-width="1.2"/></svg>
        555-318-9062
      </span>
    </div>
    <p>email: nolan@corvastadental.com</p>
    <p>addres: street-12 marlow ave.</p>
  </div>
  <div class="opening-hours">
    <svg width="20" height="20" viewBox="0 0 20 20" aria-hidden="true"><circle cx="10" cy="10" r="8.5" fill="none" stroke="var(--text-light)" stroke-width="1.6"/><polyline points="10,4.5 10,10 13.5,13" fill="none" stroke="var(--text-light)" stroke-width="1.6"/></svg>
    09:00 AM - 8:00PM
  </div>
  <p class="web-address">www.corvastadental.com</p>
  <p class="brand-name">Corvasta Dental</p>
</section>

<section class="business-card business-card--green" aria-label="Business card, green version">
  <svg class="card-shapes" width="601" height="332" viewBox="0 0 601 332" aria-hidden="true">
    <path d="M469 0 H601 V332 L492 266 Q469 252 469 228 Z" fill="var(--accent)"/>
    <rect x="0" y="89" width="15" height="29" fill="var(--accent)"/>
    <line x1="0" y1="229.5" x2="452" y2="229.5" stroke="var(--rule)" stroke-width="1"/>
    <line x1="260.5" y1="238" x2="260.5" y2="295" stroke="var(--rule)" stroke-width="1"/>
    <polyline points="0,304.5 512,304.5 548,332" fill="none" stroke="var(--rule)" stroke-width="1"/>
    <circle cx="552" cy="268" r="13" fill="none" stroke="var(--white)" stroke-width="4"/>
  </svg>
  <p class="holder-name">Dr Nolan Hale</p>
  <p class="holder-role">Director</p>
  <div class="contact-list">
    <div class="contact-phones">
      <span class="contact-item">
        <svg width="18" height="18" viewBox="0 0 18 18" aria-hidden="true"><circle cx="9" cy="9" r="8" fill="none" stroke="var(--text-light)" stroke-width="1.4"/><path d="M6 4.5 L7.6 6.8 L6.8 7.8 Q7.8 10.2 10.2 11.2 L11.2 10.4 L13.5 12 L12.4 13.4 Q8.5 13.4 5.6 9.6 Q4.4 7 6 4.5 Z" fill="var(--text-light)"/></svg>
        555-210-4837
      </span>
      <span class="contact-item">
        <svg width="12" height="20" viewBox="0 0 12 20" aria-hidden="true"><rect x="1" y="1" width="10" height="18" rx="1.5" fill="none" stroke="var(--text-light)" stroke-width="1.4"/><line x1="4" y1="16" x2="8" y2="16" stroke="var(--text-light)" stroke-width="1.2"/></svg>
        555-318-9062
      </span>
    </div>
    <p>email: nolan@corvastadental.com</p>
    <p>addres: street-12 marlow ave.</p>
  </div>
  <div class="opening-hours">
    <svg width="20" height="20" viewBox="0 0 20 20" aria-hidden="true"><circle cx="10" cy="10" r="8.5" fill="none" stroke="var(--text-light)" stroke-width="1.6"/><polyline points="10,4.5 10,10 13.5,13" fill="none" stroke="var(--text-light)" stroke-width="1.6"/></svg>
    09:00 AM - 8:00PM
  </div>
  <p class="web-address">www.corvastadental.com</p>
  <p class="brand-name">Corvasta Dental</p>
</section>

</body>
</html>
```